依頼詳細
IT企業の名刺デザインのリニューアルをお願いします。
縦位置/横位置どちらでも構いません。

現状のデザインは添付の通りです。
記載事項は、現状を踏襲ください。
表面には、加えてQVXパートナーのロゴ(添付)も掲載ください。

現状の悩みとして、情報量が多く全体的に窮屈なので
その点解消できたらと思っています。

弊社HPもご参考にされてください。
https://www.minatek.example/

※その他、各種ロゴは現状の名刺PDFより取得ください。
記載項目
<表面>
【会社名】株式会社ミナテク
【役職】営業部企画制作課 課長
クリエイティブディレクター
【名前】川辺健司・Kawabe Kenji
【資格】「ウェブ基礎レベル1」認定プロフェッショナル
【携帯】090-4815-2736
【住所】〒753-0218 山口県山口市北野台3-12 m-plaza 2F
【電話/FAX】TEL:083-547-6281 FAX:083-547-6290
【E-Mail】kawabe@minatek.example
【URL】www.minatek.example

<裏面>
東京オフィス
〒105-0392
東京都港区海岸4-2-8 ハルネビル3F

津和野オフィス
〒699-5271
島根県鹿足郡津和野町森村ロ52-7 3-B

ネオアトリエ ラボ山口運営
〒753-0218
山口県山口市北野台3-12 m-plaza 2F
0120‐571-264
希望イメージ
シンプル 複雑
単色 カラフル
暗い 明るい
日常 高級
遊び心 厳粛
未来的 伝統的
女性的 男性的
希望する色
青系、水色系
納品ファイル
• イラストレーター形式 (.ai)
補足説明
■ 選んだ理由

全体的にスッキリとしたデザインながら必要な情報が全て配置されており、
また人によって肩書や資格等の情報が多少増減してもバランスが保てそうだと感じ、
決定させていただきました。

■ 提案者全員のお礼・コメント

素晴らしいご提案を沢山頂戴し、皆様には心より感謝いたします。
社内で検討しましたが、意見が分かれて非常に決定に困りました。
貴重なお時間を当案件のご提案に割いていただきましたことに対し、改めて御礼申し上げます。
またの機会がございましたら、どうぞよろしくお願いいたします。

```html
<!DOCTYPE html>
<html lang="ja">
<head>
<meta charset="utf-8">
<title>株式会社ミナテク 名刺 表面</title>
<link rel="stylesheet" href="https://fonts.googleapis.com/css2?family=Noto+Sans+JP:wght@400;500;700&display=swap">
<style>
  :root {
    --paper: #ffffff;
    --ink: #1f1f1f;
    --brand-navy: #1d3f8f;
    --brand-sky: #3aa6dc;
    --mark-line: #222222;
    --muted: #555555;
  }
  * { margin: 0; padding: 0; box-sizing: border-box; }
  html, body {
    width: 837px; height: 1200px; overflow: hidden;
    background: var(--paper);
  }
  body {
    position: relative;
    font-family: "Noto Sans JP", sans-serif;
    color: var(--ink);
  }
  .crop-marks { position: absolute; inset: 0; }
  .crop-marks line { stroke: var(--mark-line); stroke-width: 1.2; }

  .card { position: absolute; left: 112px; top: 57px; width: 613px; height: 1015px; }

  .role {
    position: absolute; left: 20px; top: 62px;
    font-size: 13px; font-weight: 500; letter-spacing: 0.02em; white-space: nowrap;
  }
  .role-divider { color: var(--muted); margin: 0 4px; }
  .accent-bar {
    position: absolute; left: 20px; top: 90px; width: 413px; height: 6px;
    background: var(--brand-navy);
  }

  .brand {
    position: absolute; left: 478px; top: 60px;
    display: flex; align-items: center; gap: 10px;
  }
  .brand-dot {
    width: 22px; height: 22px; border-radius: 50%;
    background: var(--brand-sky);
  }
  .brand-name {
    font-size: 16px; font-weight: 500; color: var(--ink);
    letter-spacing: 0.06em;
  }

  .person { position: absolute; left: 20px; top: 138px; }
  .person-name { font-size: 34px; font-weight: 700; letter-spacing: 0.12em; line-height: 1.1; }
  .person-roman {
    display: flex; gap: 56px; margin-top: 6px;
    font-size: 11px; font-weight: 500; color: var(--muted);
  }

  .contact { position: absolute; left: 20px; top: 198px; font-size: 14px; line-height: 25.5px; }
  .company { font-size: 19px; font-weight: 700; line-height: 30px; margin-bottom: 4px; letter-spacing: 0.04em; }

  .certification {
    position: absolute; left: 20px; top: 384px;
    display: flex; align-items: center; gap: 8px;
    font-size: 11px; color: var(--muted);
  }
  .cert-badge { width: 16px; height: 16px; border-radius: 50%; border: 1.5px solid #c0392b; }
  .partner-badge {
    position: absolute; left: 506px; top: 356px; width: 26px; height: 26px;
    border-radius: 50%; border: 2px solid var(--brand-sky);
  }
</style>
</head>
<body>
  <svg class="crop-marks" width="837" height="1200" viewBox="0 0 837 1200" aria-hidden="true">
    <line x1="112" y1="0" x2="112" y2="40"/><line x1="95" y1="0" x2="95" y2="57"/>
    <line x1="0" y1="57" x2="80" y2="57"/><line x1="0" y1="40" x2="95" y2="40"/>
    <line x1="725" y1="0" x2="725" y2="40"/><line x1="742" y1="0" x2="742" y2="57"/>
    <line x1="757" y1="57" x2="837" y2="57"/><line x1="742" y1="40" x2="837" y2="40"/>
    <line x1="112" y1="1090" x2="112" y2="1200"/><line x1="95" y1="1072" x2="95" y2="1200"/>
    <line x1="0" y1="1072" x2="80" y2="1072"/><line x1="0" y1="1089" x2="95" y2="1089"/>
    <line x1="725" y1="1090" x2="725" y2="1200"/><line x1="742" y1="1072" x2="742" y2="1200"/>
    <line x1="757" y1="1072" x2="837" y2="1072"/><line x1="742" y1="1089" x2="837" y2="1089"/>
    <line x1="418" y1="0" x2="418" y2="40"/><line x1="370" y1="20" x2="466" y2="20"/>
    <line x1="418" y1="1090" x2="418" y2="1200"/><line x1="370" y1="1150" x2="466" y2="1150"/>
    <line x1="0" y1="565" x2="80" y2="565"/><line x1="30" y1="515" x2="30" y2="615"/>
    <line x1="757" y1="565" x2="837" y2="565"/><line x1="807" y1="515" x2="807" y2="615"/>
  </svg>

  <main class="card">
    <p class="role">営業部企画制作課 課長<span class="role-divider">|</span>クリエイティブディレクター</p>
    <div class="accent-bar"></div>

    <div class="brand">
      <span class="brand-dot"></span>
      <p class="brand-name">MINATEK</p>
    </div>

    <div class="person">
      <h1 class="person-name">川辺　健司</h1>
      <p class="person-roman"><span>Kawabe</span><span>Kenji</span></p>
    </div>

    <div class="contact">
      <p class="company">株式会社ミナテク</p>
      <p>〒753-0218 山口県山口市北野台3-12 m-plaza 2F</p>
      <p>TEL：090-4815-2736 / 083-547-6281</p>
      <p>FAX：083-547-6290</p>
      <p>MAIL：kawabe@minatek.example</p>
      <p>www.minatek.example</p>
    </div>

    <p class="certification">「ウェブ基礎レベル1」認定プロフェッショナル<span class="cert-badge"></span></p>
    <div class="partner-badge" role="img" aria-label="パートナー認定バッジ"></div>
  </main>
</body>
</html>
```